Résumé app needs 1 more template

Hi, I need 1 more template for my résumé app. The résumé app can be used in a browser (https://brightquill.com/resume-app) on an Koravo / Tabrix (https://apps.orvantel.com/app/id583726104) or on an Vellumos (https://market.tindrel.com/store/apps/details?id=com.brightquill.resume). The app lets the user create a résumé. It currently let's the user choose between 3 templates. I need 1 more. Please use the app first so you know how it will work.

Reason: Need more designs

Target Market(s)

Users of the app

Colors

Designer to choose colors to be used in the design.

Requirements
Must have
• original
• beautiful
• the resume template contains the data that the user can currently enter in the app (so do NOT design new features like sliders for level of experience etc)

```html
<!DOCTYPE html>
<html lang="en">
<head>
<meta charset="utf-8">
<title>Résumé Template – Graphic Designer</title>
<link href="https://fonts.googleapis.com/css2?family=Arimo:wght@700&family=Tinos:ital,wght@0,400;0,700;1,400;1,700&display=swap" rel="stylesheet">
<style>
  :root {
    --ink: #1b0e45;
    --panel: #e6e6e6;
    --band: #d3d2da;
    --white: #ffffff;
    --card: #38295e;
    --muted: #d8d4e6;
    --black: #000000;
  }
  * { margin: 0; padding: 0; box-sizing: border-box; }
  html, body { width: 928px; height: 1200px; overflow: hidden; background: var(--white); }
  .resume { position: relative; width: 928px; height: 1200px; font-family: "Tinos", "Times New Roman", serif; }

  /* Sidebar */
  .sidebar { position: absolute; left: 0; top: 0; width: 299px; height: 1200px; background: var(--panel); }
  .portrait { position: absolute; left: 41px; top: 31px; width: 220px; height: 195px; border: 3px solid var(--ink); background: linear-gradient(180deg, #e6e6e6 0%, #bdbdbd 100%); }
  .identity { position: absolute; left: 0; top: 226px; width: 299px; height: 88px; background: var(--white); text-align: center; }
  .identity .name { font-family: "Arimo", Arial, sans-serif; font-weight: 700; font-size: 42px; color: var(--ink); line-height: 1; margin-top: 10px; }
  .identity .role { font-style: italic; font-weight: 700; font-size: 26px; color: #1a1a1a; line-height: 1; margin-top: 5px; }
  .contact { position: absolute; left: 0; top: 314px; width: 299px; height: 57px; background: var(--band); text-align: center; font-style: italic; font-weight: 700; font-size: 17px; line-height: 24px; padding-top: 4px; color: #1a1a1a; }
  .address { position: absolute; left: 62px; top: 402px; width: 230px; font-style: italic; font-weight: 700; font-size: 17px; line-height: 22px; color: #1a1a1a; }
  .about-heading { position: absolute; left: 0; top: 542px; width: 299px; height: 62px; background: var(--band); padding-left: 62px; font-family: "Arimo", Arial, sans-serif; font-weight: 700; font-size: 23px; line-height: 62px; color: var(--ink); }
  .about-text { position: absolute; left: 62px; top: 633px; width: 200px; font-style: italic; font-weight: 700; font-size: 21px; line-height: 25.5px; color: #1a1a1a; }
  .sidebar-rule { position: absolute; left: 0; top: 994px; width: 299px; height: 1px; background: var(--ink); }
  .sidebar-bar { position: absolute; left: 0; top: 1157px; width: 299px; height: 13px; background: var(--ink); }

  /* Main column */
  .main { position: absolute; left: 303px; top: 0; width: 625px; height: 1200px; background: var(--ink); }
  .top-strip { position: absolute; left: 0; top: 31px; width: 625px; height: 12px; background: var(--panel); }
  .section-title { position: absolute; left: 28px; font-family: "Arimo", Arial, sans-serif; font-weight: 700; font-size: 23px; color: var(--white); line-height: 1; }
  .section-rule { position: absolute; left: 0; width: 595px; height: 1px; background: #b9b3cf; }
  .icon-badge { position: absolute; width: 116px; height: 116px; border-radius: 50%; background: var(--white); border: 2px solid #0d0626; display: flex; align-items: center; justify-content: center; }
  .icon-badge .placeholder { font-weight: 700; font-size: 11px; line-height: 14px; text-align: center; color: var(--black); }
  .entry { position: absolute; left: 213px; width: 271px; height: 70px; background: var(--card); padding: 13px 0 0 21px; color: var(--white); }
  .entry .title { font-weight: 700; font-size: 17px; line-height: 20px; letter-spacing: 0.3px; }
  .entry .sub { font-size: 14px; line-height: 18px; margin-top: 5px; color: #eae7f3; }
  .dates { position: absolute; left: 502px; font-style: italic; font-size: 14px; line-height: 18px; color: var(--muted); }
  .dates .bar { display: block; width: 1px; height: 14px; background: var(--muted); margin: 0 0 0 1px; }
  .extra-box { position: absolute; left: 213px; top: 967px; width: 382px; height: 183px; background: var(--card); }
</style>
</head>
<body>
<div class="resume">
  <aside class="sidebar">
    <div class="portrait" role="img" aria-label="Profile photo of the résumé owner"></div>
    <div class="identity">
      <div class="name">NAME</div>
      <div class="role">Graphic Designer</div>
    </div>
    <div class="contact">hello@inkfolio-mail.com<br>+1234567890</div>
    <div class="address">Address<br>Lorem ipsum dolor sit amet, consectetuer adipiscing elit, sed diam nonummy nibh euismod</div>
    <div class="about-heading">About Me</div>
    <p class="about-text">Lorem ipsum dolor sit amet, consectetuer adipiscing elit, sed diam nonummy nibh euismod tincidunt ut laoreet dolore magna aliquam erat volutpat. Ut wisi enim ad minim veniam, quis nostrud exerci tation ullamcorper</p>
    <div class="sidebar-rule"></div>
    <div class="sidebar-bar"></div>
  </aside>

  <main class="main">
    <div class="top-strip"></div>

    <!-- Experience -->
    <h2 class="section-title" style="top:80px;">Experience</h2>
    <div class="section-rule" style="top:108px;"></div>
    <div class="icon-badge" style="left:28px; top:251px;">
      <svg width="74" height="56" viewBox="0 0 74 56" aria-hidden="true">
        <rect x="25" y="2" width="24" height="10" rx="2" fill="none" stroke="#1b0e45" stroke-width="4"/>
        <rect x="4" y="12" width="66" height="40" rx="5" fill="#dde2e0" stroke="#1b0e45" stroke-width="4"/>
        <line x1="4" y1="28" x2="70" y2="28" stroke="#1b0e45" stroke-width="4"/>
        <rect x="14" y="24" width="6" height="10" fill="#1b0e45"/>
        <rect x="54" y="24" width="6" height="10" fill="#1b0e45"/>
      </svg>
    </div>
    <div class="entry" style="top:138px;"><div class="title">Graphic Designer</div><div class="sub">Company 4</div></div>
    <div class="dates" style="top:146px;">Till Now<span class="bar"></span>2015</div>
    <div class="entry" style="top:229px;"><div class="title">Graphic Designer</div><div class="sub">Company 3</div></div>
    <div class="dates" style="top:237px;">2015<span class="bar"></span>2014</div>
    <div class="entry" style="top:319px;"><div class="title">Graphic Designer</div><div class="sub">Company 2</div></div>
    <div class="dates" style="top:327px;">2014<span class="bar"></span>2011</div>
    <div class="entry" style="top:409px;"><div class="title">Graphic Designer</div><div class="sub">Company 1</div></div>
    <div class="dates" style="top:417px;">2011<span class="bar"></span>2010</div>

    <!-- Education -->
    <h2 class="section-title" style="top:532px;">Education</h2>
    <div class="section-rule" style="top:560px;"></div>
    <div class="icon-badge" style="left:29px; top:658px;">
      <svg width="76" height="52" viewBox="0 0 76 52" aria-hidden="true">
        <path d="M4 8 Q20 2 38 8 Q56 2 72 8 V46 Q56 40 38 46 Q20 40 4 46 Z" fill="none" stroke="#1b0e45" stroke-width="4" stroke-linejoin="round"/>
        <line x1="38" y1="8" x2="38" y2="46" stroke="#1b0e45" stroke-width="4"/>
        <path d="M10 16 Q22 12 32 16 M10 24 Q22 20 32 24 M10 32 Q22 28 32 32 M44 16 Q54 12 66 16 M44 24 Q54 20 66 24 M44 32 Q54 28 66 32" fill="none" stroke="#1b0e45" stroke-width="3"/>
        <path d="M2 46 V50 H74 V46" fill="none" stroke="#1b0e45" stroke-width="3"/>
      </svg>
    </div>
    <div class="entry" style="top:591px;"><div class="title">College name</div><div class="sub">XXXXX</div></div>
    <div class="dates" style="top:599px;">2009<span class="bar"></span>2005</div>
    <div class="entry" style="top:681px;"><div class="title">School name</div><div class="sub">XXXXX</div></div>
    <div class="dates" style="top:689px;">2005<span class="bar"></span>2003</div>
    <div class="entry" style="top:772px;"><div class="title">School name</div><div class="sub">XXXXX</div></div>
    <div class="dates" style="top:780px;">2003<span class="bar"></span>2002</div>

    <!-- Something Else -->
    <h2 class="section-title" style="top:914px;">Something Else</h2>
    <div class="section-rule" style="top:942px;"></div>
    <div class="icon-badge" style="left:29px; top:1001px;">
      <div class="placeholder">Placeholder<br>for Icon<br>based on title</div>
    </div>
    <div class="extra-box"></div>
  </main>
</div>
</body>
</html>
```